Personal Care and Home care ingredients Brochure

We need a flyer or brochure of the of chemicals we distribute for the manufacturing of personal care products such as shampoos, liquid soaps, creams, lotions, conditioners, hand sanitizer, Hair Jellys, etc and for Home care products such as, liquid soaps, desinfectants, cleaners, stain removers,etc.
The idea is to send this pdf brochure via email and companies feel very confortable with the impression it gives. We want to call attention.
Target Market(s)
Companies that manufactures cosmetics, personal care products and home care products.
Colors
Designer to choose colors to be used in the design.
Requirements
Must have
- Images that refers to the skin, hair, cleaning, washing

```html
<!DOCTYPE html>
<html lang="es">
<head>
<meta charset="utf-8">
<title>Verdafonate – Folleto</title>
<link href="https://fonts.googleapis.com/css2?family=Lato:wght@400;700;900&display=swap" rel="stylesheet">
<style>
  :root{
    --bg:#e2e2e2;
    --paper:#f3f3f3;
    --green:#2a9a7a;
    --green-light:#5fba9c;
    --green-dark:#1f7f66;
    --navy:#1e2a44;
    --ink:#1c1c1c;
  }
  *{margin:0;padding:0;box-sizing:border-box}
  html,body{width:1200px;height:700px;overflow:hidden;background:var(--bg);font-family:'Lato',sans-serif}
  .spread{position:absolute;left:100px;top:100px;width:1000px;height:500px;display:flex;box-shadow:0 18px 40px rgba(0,0,0,.18)}
  .panel{position:relative;width:500px;height:500px;overflow:hidden}
  .panel--photo{background:linear-gradient(120deg,#6fa2c9 0%,#c9d7e6 35%,#f1dcd3 55%,#8fb6d6 80%,#4d7fb0 100%)}
  .panel--info{background:linear-gradient(180deg,#f7f7f7,#ececec)}
  .decor{position:absolute;inset:0;width:100%;height:100%}
  .copy{position:absolute;left:40px;top:150px;width:440px;color:var(--ink)}
  .copy h2{font-weight:900;color:var(--green);font-size:18px;letter-spacing:.2px;line-height:1.15}
  .copy h2 .plain{font-weight:700}
  .copy .line{display:block;white-space:nowrap}
  .copy .sub{font-size:10px;font-weight:700;margin:3px 0 14px}
  .benefits{list-style:none;font-size:10.5px;font-weight:700;line-height:1.3;margin-top:6px}
  .brand{position:absolute;right:32px;top:318px;display:flex;align-items:center;gap:6px}
  .brand__mark{width:14px;height:14px;background:var(--green)}
  .brand__name{font-weight:900;font-size:15px;color:var(--navy);letter-spacing:.5px}
</style>
</head>
<body>
  <main class="spread">
    <section class="panel panel--photo" role="img" aria-label="Fotografía: clienta sonriente en un pasillo de supermercado sosteniendo una botella de detergente y levantando el pulgar"></section>
    <section class="panel panel--info">
      <svg class="decor" viewBox="0 0 500 500" aria-hidden="true">
        <polygon points="230,75 250,50 372,50 352,75" fill="var(--green-light)"/>
        <polygon points="352,75 372,50 400,22 388,60" fill="var(--green-dark)"/>
        <polygon points="400,22 470,22 470,44 388,60" fill="var(--green-light)"/>
        <polygon points="470,22 500,22 500,44 470,44" fill="#bfd9cf"/>
        <polygon points="0,500 0,440 60,440 30,470 0,470" fill="var(--green-light)"/>
        <polygon points="0,470 30,470 60,440 120,440 90,470" fill="var(--green-light)"/>
        <polygon points="0,470 90,470 60,500 0,500" fill="var(--navy)"/>
      </svg>
      <div class="copy">
        <h2>VERDAFONATE</h2>
        <p class="sub">Seguridad y Suavidad</p>
        <h2>IMPARTE EL BALANCE PERFECTO</h2>
        <p class="sub">Suave a la piel y a los textiles.</p>
        <h2><span class="line">El VERDAFONATE <span class="plain">es un surfactante mas verde.</span></span><span class="line">Huella mas verde</span></h2>
        <ul class="benefits">
          <li>Eco-amigable</li>
          <li>Hecho de fuentes renovables</li>
          <li>Sustentable</li>
          <li>Biodegradable</li>
        </ul>
      </div>
      <div class="brand">
        <span class="brand__mark"></span>
        <span class="brand__name">NOVAQUIM</span>
      </div>
    </section>
  </main>
</body>
</html>
```